Quick Banner Ad Job for IT Services Company

Need a collection of banner ads based around a common theme and message.

Main Theme.

IT Support and Managed Services - IT support you can rely on.
Free remote monitoring and alerting*
*conditions apply <-- this in small text

Secondary Content

Our customers are attracted by our exceptional level of customer service and trust us in providing them with support and advice over a long term relationship.

Note:
* Logos and colours attached. Only use these colours.
* Font is to be Myriad Pro

* Delivery will require the following sizes.
Leaderboard: 728×90
Medium Rectangle: 300×250
Wide Skyscraper: 160×600

Do the initial draft in leaderboard, other sizes can be worked once we have an agreed design for the main

Final delivery will also need to be in an editable format, not just final images.

Industry/Entity Type

It Company

```html
<!DOCTYPE html>
<html lang="en">
<head>
<meta charset="utf-8">
<title>Leaderboard Animation Storyboard</title>
<link rel="stylesheet" href="https://fonts.googleapis.com/css2?family=Source+Sans+3:ital,wght@0,400;0,600;0,700;1,400&display=swap">
<style>
  :root {
    --brand-blue: #0a78c0;
    --brand-navy: #0d2d4d;
    --title-grey: #7d8a96;
    --frame-line: #cfd6dc;
    --paper: #ffffff;
  }
  * { box-sizing: border-box; margin: 0; padding: 0; }
  html, body { width: 1200px; height: 1200px; overflow: hidden; background: var(--paper); }
  body { position: relative; font-family: "Source Sans 3", sans-serif; }

  .note { position: absolute; left: 59px; top: 48px; color: var(--brand-blue); font-style: italic; font-size: 33px; line-height: 40px; }
  .label { position: absolute; color: var(--brand-blue); font-style: italic; font-size: 34px; transform: translateX(-50%); letter-spacing: 1px; }

  /* left column: blue banner frames */
  .banner { position: absolute; left: 18px; width: 582px; height: 72px; border: 1px solid var(--frame-line); background: var(--paper); overflow: hidden; }
  .banner-field { position: absolute; inset: 0; width: 100%; height: 100%; }
  .banner-title { position: absolute; left: 14px; top: 6px; font-size: 22px; font-weight: 700; color: #fff; letter-spacing: -0.4px;
    text-shadow: -1px -1px 0 #2a5f9a, 1px -1px 0 #2a5f9a, -1px 1px 0 #2a5f9a, 1px 1px 0 #2a5f9a; white-space: nowrap; }
  .banner-copy { position: absolute; left: 14px; top: 42px; font-size: 10.5px; line-height: 13.5px; color: #fff; white-space: nowrap; }
  .banner-story { position: absolute; left: 21px; top: 19px; font-size: 10px; line-height: 13px; color: #fff; }
  .faded { opacity: 0.3; }

  .brand { position: absolute; display: flex; align-items: center; gap: 8px; }
  .brand-dot { width: 36px; height: 36px; border-radius: 50%; background: var(--brand-blue); flex: none; }
  .brand-name { font-size: 40px; font-weight: 700; color: var(--brand-navy); letter-spacing: -1px; line-height: 1; }
  .brand-tag { position: absolute; right: 0; bottom: -11px; font-size: 9.5px; color: var(--brand-navy); }
  .banner .brand { right: 12px; top: 12px; }

  /* right column: white text frames */
  .frame { position: absolute; left: 617px; width: 583px; height: 72px; border: 1px solid var(--frame-line); border-right: none; background: var(--paper); overflow: hidden; }
  .frame-title { position: absolute; left: 22px; top: 2px; font-size: 36px; font-weight: 700; color: var(--brand-navy); white-space: nowrap; letter-spacing: 0.2px; }
  .frame-title.is-pending { color: var(--title-grey); }
  .frame-line { position: absolute; top: 47px; font-size: 14px; font-weight: 600; color: var(--brand-blue); white-space: nowrap; }
  .line-one { left: 24px; }
  .line-two { left: 202px; }
  .line-three { left: 447px; font-weight: 400; }
  .frame-story { position: absolute; left: 0; right: 0; top: 15px; text-align: center; font-size: 15px; font-weight: 600; line-height: 18px; color: var(--brand-blue); }
  .frame .brand { left: 50%; top: 12px; transform: translateX(-50%); }
</style>
</head>
<body>

<p class="note">Hi this is the animation step by step<br>pls send me an email to send you the animated one.<br>studio.mail@example.com</p>

<span class="label" style="left:280px; top:300px;">start</span>
<span class="label" style="left:908px; top:178px;">start</span>

<!-- Left sequence -->
<div class="banner" style="top:350px;">
  <svg class="banner-field" viewBox="0 0 582 72" preserveAspectRatio="none" aria-hidden="true"><path d="M0 0H398C360 28 330 55 301 72H0Z" fill="var(--brand-blue)"/></svg>
  <div class="brand"><span class="brand-dot"></span><span class="brand-name">Orvia</span><span class="brand-tag">IT Support</span></div>
</div>

<div class="banner" style="top:438px;">
  <svg class="banner-field" viewBox="0 0 582 72" preserveAspectRatio="none" aria-hidden="true"><path d="M0 0H398C360 28 330 55 301 72H0Z" fill="var(--brand-blue)"/></svg>
  <div class="banner-title faded" style="opacity:.55">IT Support and Managed Services</div>
  <div class="brand"><span class="brand-dot"></span><span class="brand-name">Orvia</span><span class="brand-tag">IT Support</span></div>
</div>

<div class="banner" style="top:526px;">
  <svg class="banner-field" viewBox="0 0 582 72" preserveAspectRatio="none" aria-hidden="true"><path d="M0 0H398C360 28 330 55 301 72H0Z" fill="var(--brand-blue)"/></svg>
  <div class="banner-title">IT Support and Managed Services</div>
  <div class="banner-copy faded" style="opacity:.6">- IT support you can rely on. Free remote monitoring and alerting*<br>*conditions apply</div>
  <div class="brand"><span class="brand-dot"></span><span class="brand-name">Orvia</span><span class="brand-tag">IT Support</span></div>
</div>

<div class="banner" style="top:614px;">
  <svg class="banner-field" viewBox="0 0 582 72" preserveAspectRatio="none" aria-hidden="true"><path d="M0 0H398C360 28 330 55 301 72H0Z" fill="var(--brand-blue)"/></svg>
  <div class="banner-title">IT Support and Managed Services</div>
  <div class="banner-copy">- IT support you can rely on. Free remote monitoring and alerting*<br>*conditions apply</div>
  <div class="brand"><span class="brand-dot"></span><span class="brand-name">Orvia</span><span class="brand-tag">IT Support</span></div>
</div>

<div class="banner" style="top:702px;">
  <svg class="banner-field" viewBox="0 0 582 72" preserveAspectRatio="none" aria-hidden="true"><path d="M0 0H398C360 28 330 55 301 72H0Z" fill="var(--brand-blue)"/></svg>
  <div class="banner-story faded">Our customers are attracted by our exceptional level of customer<br>service and trust us in providing them with support and advice<br>over a long term relationship.</div>
  <div class="brand"><span class="brand-dot"></span><span class="brand-name">Orvia</span><span class="brand-tag">IT Support</span></div>
</div>

<div class="banner" style="top:790px;">
  <svg class="banner-field" viewBox="0 0 582 72" preserveAspectRatio="none" aria-hidden="true"><path d="M0 0H398C360 28 330 55 301 72H0Z" fill="var(--brand-blue)"/></svg>
  <div class="banner-story">Our customers are attracted by our exceptional level of customer<br>service and trust us in providing them with support and advice<br>over a long term relationship.</div>
  <div class="brand"><span class="brand-dot"></span><span class="brand-name">Orvia</span><span class="brand-tag">IT Support</span></div>
</div>

<div class="banner" style="top:878px;">
  <svg class="banner-field" viewBox="0 0 582 72" preserveAspectRatio="none" aria-hidden="true"><path d="M0 0H398C360 28 330 55 301 72H0Z" fill="var(--brand-blue)"/></svg>
  <div class="brand"><span class="brand-dot"></span><span class="brand-name">Orvia</span><span class="brand-tag">IT Support</span></div>
</div>

<span class="label" style="left:258px; top:962px;">end</span>

<!-- Right sequence -->
<div class="frame" style="top:226px;">
  <div class="frame-title is-pending">IT Support and Managed Services</div>
</div>

<div class="frame" style="top:298px;">
  <div class="frame-title">IT Support and Managed Services</div>
  <div class="frame-line line-one faded">IT support you can rely on.</div>
</div>

<div class="frame" style="top:386px;">
  <div class="frame-title">IT Support and Managed Services</div>
  <div class="frame-line line-one">IT support you can rely on.</div>
</div>

<div class="frame" style="top:474px;">
  <div class="frame-title">IT Support and Managed Services</div>
  <div class="frame-line line-one">IT support you can rely on.</div>
  <div class="frame-line line-two faded">Free remote monitoring and alerting*</div>
</div>

<div class="frame" style="top:562px;">
  <div class="frame-title">IT Support and Managed Services</div>
  <div class="frame-line line-one">IT support you can rely on.</div>
  <div class="frame-line line-two">Free remote monitoring and alerting*</div>
</div>

<div class="frame" style="top:650px;">
  <div class="frame-title">IT Support and Managed Services</div>
  <div class="frame-line line-one">IT support you can rely on.</div>
  <div class="frame-line line-two">Free remote monitoring and alerting*</div>
  <div class="frame-line line-three faded">*conditions apply</div>
</div>

<div class="frame" style="top:738px;">
  <div class="frame-title">IT Support and Managed Services</div>
  <div class="frame-line line-one">IT support you can rely on.</div>
  <div class="frame-line line-two">Free remote monitoring and alerting*</div>
  <div class="frame-line line-three">*conditions apply</div>
</div>

<div class="frame" style="top:826px;">
  <div class="frame-title faded">IT Support and Managed Services</div>
  <div class="frame-line line-one faded">IT support you can rely on.</div>
  <div class="frame-line line-two faded">Free remote monitoring and alerting*</div>
  <div class="frame-line line-three faded">*conditions apply</div>
  <div class="frame-story faded" style="top:9px; opacity:.4">Our customers are attracted by our exceptional level of customer service and<br>trust us in providing them with support and advice over a long term relationship.</div>
</div>

<div class="frame" style="top:914px;">
  <div class="frame-story">Our customers are attracted by our exceptional level of customer service and<br>trust us in providing them with support and advice over a long term relationship.</div>
</div>

<div class="frame" style="top:1002px;">
  <div class="frame-story faded" style="opacity:.2">Our customers are attracted by our exceptional level of customer service and<br>trust us in providing them with support and advice over a long term relationship.</div>
  <div class="brand" style="opacity:.8"><span class="brand-dot"></span><span class="brand-name">Orvia</span><span class="brand-tag">IT Support</span></div>
</div>

<div class="frame" style="top:1091px;">
  <div class="brand"><span class="brand-dot"></span><span class="brand-name">Orvia</span><span class="brand-tag">IT Support</span></div>
</div>

<span class="label" style="left:908px; top:1158px;">end</span>

</body>
</html>
```